New Business Card Design Project

We want a modern business card that catches the attention of other remodeling companies as well as homeowners. We would like it to be informative but still simple.

Target Market(s)

Residential and other Business's

Contact Information for Business Card

TidyKraft
Phone number is 5152947718
Address is
4817 SW 3rd Lane
Des Moines, Iowa 50313
email is tidykraftia@mailorbit.net

Requirements
Must have
• Our tagline
• Honest | Professional | Affordable

```html
<!DOCTYPE html>
<html lang="en">
<head>
<meta charset="utf-8">
<title>TidyKraft Business Card</title>
<link rel="stylesheet" href="https://fonts.googleapis.com/css2?family=Lato:wght@400;700&family=Oswald:wght@500&display=swap">
<style>
  :root {
    --backdrop: #b9b9b9;
    --brand-orange: #cc4e00;
    --brand-blue: #0066cc;
    --card-white: #ffffff;
    --text-light: #ffffff;
  }
  * { margin: 0; padding: 0; box-sizing: border-box; }
  html, body { width: 1200px; height: 802px; overflow: hidden; }
  body { background: var(--backdrop); font-family: "Lato", sans-serif; position: relative; }

  .card {
    position: absolute;
    top: 274px;
    width: 443px;
    height: 265px;
    box-shadow: 2px 3px 6px rgba(0,0,0,0.35);
    overflow: hidden;
  }
  .card-front { left: 136px; background: var(--brand-orange); }
  .card-back { left: 624px; background: var(--card-white); }

  .symbol-area { position: absolute; left: 0; top: 0; width: 240px; height: 265px; }

  .contact {
    position: absolute;
    right: 22px;
    text-align: right;
    color: var(--text-light);
    font-size: 12.5px;
    line-height: 16px;
  }
  .holder { top: 40px; }
  .holder .name { font-weight: 700; font-size: 16px; line-height: 18px; letter-spacing: 0.2px; }
  .company { top: 128px; }
  .company .company-name { font-weight: 700; }
  .reach { top: 202px; }
  .reach .line { display: flex; justify-content: flex-end; align-items: center; gap: 5px; height: 18px; }
  .reach svg { width: 14px; height: 13px; }

  .brand {
    position: absolute;
    left: 0; right: 0;
    top: 106px;
    text-align: center;
  }
  .brand-name {
    font-family: "Lato", sans-serif;
    font-weight: 700;
    font-size: 42px;
    line-height: 46px;
    letter-spacing: 1px;
    color: var(--brand-blue);
  }
  .tagline {
    margin-top: 4px;
    font-family: "Oswald", sans-serif;
    font-weight: 500;
    font-size: 15px;
    letter-spacing: 0.6px;
    color: var(--brand-blue);
  }
  .tagline .divider { color: var(--brand-orange); padding: 0 3px; }
</style>
</head>
<body>
  <section class="card card-front">
    <svg class="symbol-area" viewBox="0 0 240 265" role="img" aria-label="Brand symbol area in blue and white">
      <polygon points="0,0 140,0 170,265 0,265" fill="var(--brand-blue)"/>
    </svg>

    <div class="contact holder">
      <p class="name">REID HALVORSEN</p>
      <p class="role">Managing Director</p>
    </div>

    <div class="contact company">
      <p class="company-name">TIDYKRAFT</p>
      <p>4817 SW 3rd Lane</p>
      <p>Des Moines, Iowa 50313</p>
    </div>

    <div class="contact reach">
      <p class="line">5152947718
        <svg viewBox="0 0 14 14" aria-hidden="true"><rect x="0.75" y="0.75" width="12.5" height="12.5" rx="2" fill="none" stroke="#fff" stroke-width="1.3"/><path d="M4.2 3.2l1.4 0 .7 1.9-.9.7c.5 1 1.3 1.8 2.3 2.3l.7-.9 1.9.7v1.4c0 .4-.4.7-.8.7C6.3 9.9 4 7.6 3.5 4c0-.4.3-.8.7-.8z" fill="#fff"/></svg>
      </p>
      <p class="line">tidykraftia@mailorbit.net
        <svg viewBox="0 0 14 11" aria-hidden="true"><rect x="0" y="0" width="14" height="11" fill="#fff"/><path d="M0.5 0.8L7 6l6.5-5.2" fill="none" stroke="var(--brand-orange)" stroke-width="1.2"/></svg>
      </p>
    </div>
  </section>

  <section class="card card-back">
    <div class="brand">
      <p class="brand-name">TIDYKRAFT</p>
      <p class="tagline">HONEST<span class="divider">|</span>PROFESSIONAL<span class="divider">|</span>AFFORDABLE</p>
    </div>
  </section>
</body>
</html>
```